Bref créative
Business card and stationary design for home inspector
Keystone Ridge Home Inspection LLC
Professional
Walter Brunow
Owner/Founder
287 Fenwick Lane
Mooresville, NC 28942
walt@KeystoneRidgeHomeInspection.example
www.KeystoneRidgeHomeInspection.example
NC Home Inspector lic #6817
NC General Contractor lic # 58093
i would like to see both single and double sided business cards.... im not sure which i want yet... if you submit double sided maybe have my logo on the backside....

```html
<!DOCTYPE html>
<html lang="en">
<head>
<meta charset="utf-8">
<title>Keystone Ridge Home Inspection — Stationery</title>
<link href="https://fonts.googleapis.com/css2?family=Open+Sans:wght@400;700&display=swap" rel="stylesheet">
<style>
  :root{
    --navy:#1b4f86;
    --navy-deep:#0f3461;
    --sky:#cfdcea;
    --mist:#e9eef4;
    --paper:#ffffff;
    --grey-flap:#7d8187;
    --ink:#4a4f57;
    --stage:#efece6;
  }
  *{box-sizing:border-box;margin:0;padding:0}
  html,body{width:1200px;height:446px;overflow:hidden;background:var(--stage);font-family:"Open Sans",Arial,sans-serif}
  .sheet{position:absolute;background:var(--paper);box-shadow:0 2px 5px rgba(0,0,0,.18);overflow:hidden}
  .sheet svg.art{position:absolute;inset:0;width:100%;height:100%}
  .brand{position:absolute;display:flex;align-items:center;gap:4px;color:var(--navy);font-weight:700;text-transform:uppercase;line-height:1.05}
  .brand .dot{border-radius:50%;border:2px solid var(--navy);flex:none}
  .brand.on-dark{color:var(--paper)}
  .brand.on-dark .dot{border-color:var(--paper)}
  .contact{position:absolute;color:var(--ink);line-height:1.45}
  .ghost-mark{position:absolute;border-radius:50%;border:10px solid var(--mist)}
</style>
</head>
<body>

<!-- Business card front -->
<div class="sheet card-front" style="left:12px;top:232px;width:108px;height:52px">
  <svg class="art" viewBox="0 0 108 52" preserveAspectRatio="none">
    <path d="M80 0 H108 V52 H62 C84 38 90 18 80 0Z" fill="var(--navy)"/>
    <path d="M75 0 H80 C90 18 84 38 62 52 H56 C78 38 84 18 75 0Z" fill="var(--sky)"/>
  </svg>
  <div class="brand" style="left:6px;top:7px;font-size:4.2px"><span class="dot" style="width:9px;height:9px;border-width:1.2px"></span><span>Keystone Ridge<br>Home Inspection</span></div>
  <div class="contact" style="left:6px;top:24px;font-size:2.6px">Walter Brunow · Owner/Founder<br>287 Fenwick Lane, Mooresville, NC 28942<br>walt@KeystoneRidgeHomeInspection.example<br>www.KeystoneRidgeHomeInspection.example</div>
</div>

<!-- Business card back -->
<div class="sheet card-back" style="left:12px;top:312px;width:108px;height:53px;background:var(--navy)">
  <svg class="art" viewBox="0 0 108 53" preserveAspectRatio="none">
    <path d="M0 40 C30 30 70 52 108 36 V53 H0Z" fill="var(--navy-deep)"/>
  </svg>
  <div class="brand on-dark" style="left:28px;top:19px;font-size:4.6px"><span class="dot" style="width:11px;height:11px;border-width:1.4px"></span><span>Keystone Ridge<br>Home Inspection</span></div>
</div>

<!-- Letterhead option 1 -->
<div class="sheet letterhead-one" style="left:163px;top:19px;width:300px;height:413px">
  <svg class="art" viewBox="0 0 300 413" preserveAspectRatio="none">
    <path d="M0 372 C90 352 200 395 300 360 V413 H0Z" fill="var(--sky)"/>
    <path d="M0 384 C100 366 200 405 300 374 V413 H0Z" fill="var(--navy)"/>
  </svg>
  <div class="brand" style="left:16px;top:18px;font-size:7px"><span class="dot" style="width:17px;height:17px"></span><span>Keystone Ridge<br>Home Inspection</span></div>
  <div class="contact" style="left:186px;top:16px;font-size:4px">walt@KeystoneRidgeHomeInspection.example<br>www.KeystoneRidgeHomeInspection.example<br>287 Fenwick Lane<br>Mooresville, NC 28942<br>NC Home Inspector lic #6817<br>NC General Contractor lic # 58093</div>
  <div class="ghost-mark" style="left:95px;top:150px;width:110px;height:110px"></div>
</div>

<!-- Letterhead option 2 -->
<div class="sheet letterhead-two" style="left:475px;top:19px;width:300px;height:413px">
  <svg class="art" viewBox="0 0 300 413" preserveAspectRatio="none">
    <path d="M0 0 H22 C8 90 48 200 14 413 H0Z" fill="var(--sky)"/>
    <path d="M0 0 H14 C0 90 38 200 6 413 H0Z" fill="var(--navy)"/>
    <path d="M0 413 C60 395 120 405 140 413Z" fill="var(--navy)"/>
  </svg>
  <div class="brand" style="left:96px;top:18px;font-size:7px"><span class="dot" style="width:17px;height:17px"></span><span>Keystone Ridge<br>Home Inspection</span></div>
  <div class="ghost-mark" style="left:100px;top:150px;width:110px;height:110px"></div>
  <div class="contact" style="left:62px;top:385px;font-size:3.8px;text-align:center;width:200px">287 Fenwick Lane, Mooresville, NC 28942 · walt@KeystoneRidgeHomeInspection.example<br>www.KeystoneRidgeHomeInspection.example</div>
</div>

<!-- Envelope, blue flap -->
<div class="sheet envelope-blue" style="left:830px;top:19px;width:353px;height:96px">
  <svg class="art" viewBox="0 0 353 96" preserveAspectRatio="none">
    <path d="M0 0 H353 V30 L176 62 L0 30Z" fill="var(--navy)"/>
  </svg>
  <div class="brand on-dark" style="left:150px;top:20px;font-size:4.8px"><span class="dot" style="width:11px;height:11px;border-width:1.4px"></span><span>Keystone Ridge<br>Home Inspection</span></div>
</div>

<!-- Envelope, grey flap -->
<div class="sheet envelope-grey" style="left:830px;top:120px;width:353px;height:108px">
  <svg class="art" viewBox="0 0 353 108" preserveAspectRatio="none">
    <path d="M0 0 H353 V30 L176 64 L0 30Z" fill="var(--grey-flap)"/>
  </svg>
</div>

<!-- Envelope, white flap with mark -->
<div class="sheet envelope-white" style="left:830px;top:240px;width:353px;height:108px">
  <svg class="art" viewBox="0 0 353 108" preserveAspectRatio="none">
    <path d="M0 0 L176 58 L353 0" fill="none" stroke="#d9dde2" stroke-width="1"/>
  </svg>
  <div class="brand" style="left:150px;top:34px;font-size:4.8px"><span class="dot" style="width:11px;height:11px;border-width:1.4px"></span><span>Keystone Ridge<br>Home Inspection</span></div>
</div>

<!-- Envelope front -->
<div class="sheet envelope-front" style="left:792px;top:360px;width:276px;height:68px">
  <svg class="art" viewBox="0 0 276 68" preserveAspectRatio="none">
    <path d="M0 56 C80 48 190 66 276 52 V68 H0Z" fill="var(--navy)"/>
  </svg>
  <div class="brand" style="left:8px;top:7px;font-size:5px"><span class="dot" style="width:12px;height:12px;border-width:1.5px"></span><span>Keystone Ridge<br>Home Inspection</span></div>
  <div class="contact" style="left:8px;top:25px;font-size:3.2px">287 Fenwick Lane<br>Mooresville, NC 28942</div>
</div>

</body>
</html>
```